Real Estate Marketing Company Needs 1 Page 8.5x11 Price List Flyer Design

We need a 1 page 8.5in x 11in price list flyer that is intended for drop off at local offices. This is intended to show all the services we offer including pricing to potential new clients. It should be separated into sections for the different services we offer. I'd also like some photos and our Logo on the list to make it look nice so its not all text. Try to incorporate the logo colors in the design.

Industry/Entity Type

Real Estate

Requirements
Must have
• Price List
• Photos
• Logo
• website address

```html
<!DOCTYPE html>
<html lang="en">
<head>
<meta charset="utf-8">
<title>Open Gate Photography – Price List</title>
<link href="https://fonts.googleapis.com/css2?family=Cinzel:wght@400;600&family=Arimo:wght@400;700&display=swap" rel="stylesheet">
<style>
  :root{
    --backdrop:#595a5c;
    --paper:#ffffff;
    --brand-red:#a31f24;
    --ink:#111111;
    --frame-coral:#e07a70;
    --frame-peach:#eda78a;
    --frame-sage:#8cc0a5;
    --frame-cream:#ece3c4;
    --frame-plum:#4a2530;
    --mat:#f4efe2;
  }
  *{box-sizing:border-box;margin:0;padding:0}
  html,body{width:987px;height:1200px;overflow:hidden;background:var(--backdrop)}
  .flyer{position:absolute;left:107px;top:88px;width:788px;height:1019px;background:var(--paper);overflow:hidden;font-family:"Arimo",Arial,sans-serif;color:var(--ink)}
  .garden-strip{position:absolute;left:0;top:0;width:45px;height:100%;
    background:linear-gradient(180deg,#6d8a4c 0%,#3f6a3a 30%,#3a7fa8 55%,#2f8fbf 70%,#6f8c55 85%,#a9917a 100%)}
  .poolhouse-photo{position:absolute;left:538px;top:0;width:250px;height:100%;
    background:linear-gradient(180deg,#5e8a3a 0%,#7ea050 28%,#bfc4c0 40%,#e7e3d2 52%,#8d9088 60%,#2f95c7 66%,#3aa2cf 76%,#6b8a45 86%,#9a6a5e 100%)}
  .brand{position:absolute;left:55px;top:48px;width:190px;text-align:center}
  .brand-mark{width:62px;height:62px;border-radius:50%;background:var(--ink);margin:0 auto 8px}
  .brand-name{font-family:"Cinzel",serif;font-weight:400;font-size:22px;letter-spacing:.5px;line-height:1.05;color:var(--ink)}
  .frame{position:absolute;padding:10px;box-shadow:0 2px 4px rgba(0,0,0,.35)}
  .frame .mat{width:100%;height:100%;background:var(--mat);padding:6px}
  .frame .photo{width:100%;height:100%}
  .coral{background:var(--frame-coral)} .peach{background:var(--frame-peach)}
  .sage{background:var(--frame-sage)} .cream{background:var(--frame-cream)}
  .plum{background:var(--frame-plum)}
  .section-title{position:absolute;left:62px;font-family:"Cinzel",serif;font-weight:400;font-size:14.5px;color:var(--brand-red);letter-spacing:.3px}
  .price-list{position:absolute;left:79px;width:436px;list-style:none;font-size:12.3px;line-height:15.7px}
  .price-list li{display:flex;justify-content:space-between}
  .price-list li::before{content:"•";margin-right:4px}
  .price-list .label{flex:1}
  .price{color:var(--brand-red);font-weight:700}
  .note{position:absolute;left:87px;font-size:11.5px;font-weight:700;line-height:15.7px}
  .website{position:absolute;left:62px;top:988px;font-family:"Cinzel",serif;font-size:12.5px;color:var(--brand-red);letter-spacing:.3px}
</style>
</head>
<body>
<main class="flyer">
  <div class="garden-strip" role="img" aria-label="Photo of garden with blue spruce, flowers and pool edge"></div>
  <div class="poolhouse-photo" role="img" aria-label="Photo of pool house with French doors, pool and pink roses"></div>

  <div class="brand">
    <div class="brand-mark"></div>
    <div class="brand-name">Open Gate<br>Photography</div>
  </div>

  <div class="frame coral" style="left:242px;top:107px;width:86px;height:81px"><div class="mat"><div class="photo" role="img" aria-label="Photo of a bedroom interior" style="background:linear-gradient(135deg,#c9a47a,#8a6a4e)"></div></div></div>
  <div class="frame peach" style="left:348px;top:36px;width:171px;height:152px;padding:14px"><div class="mat"><div class="photo" role="img" aria-label="Photo of a living room with chandelier and fireplace" style="background:linear-gradient(135deg,#d9c2a0,#7d5a3e)"></div></div></div>
  <div class="frame sage" style="left:539px;top:35px;width:216px;height:249px;padding:18px"><div class="mat"><div class="photo" role="img" aria-label="Photo of a bright great room with tall windows" style="background:linear-gradient(180deg,#e8e2d6,#9c8f7f)"></div></div></div>
  <div class="frame cream" style="left:163px;top:203px;width:120px;height:185px;padding:12px"><div class="mat"><div class="photo" role="img" aria-label="Floor plan drawing of two floors" style="background:#ffffff;border:1px solid #bbb"></div></div></div>
  <div class="frame sage" style="left:300px;top:204px;width:219px;height:151px;padding:14px"><div class="mat"><div class="photo" role="img" aria-label="Photo of an estate with pool and patio" style="background:linear-gradient(180deg,#4f86c9,#c9b396 55%,#5aa7c8)"></div></div></div>
  <div class="frame cream" style="left:535px;top:299px;width:137px;height:149px;padding:14px"><div class="mat"><div class="photo" role="img" aria-label="Aerial photo of a house surrounded by forest" style="background:linear-gradient(180deg,#4d7f3a,#2f5a2a)"></div></div></div>
  <div class="frame plum" style="left:300px;top:367px;width:88px;height:98px;padding:12px"><div class="mat"><div class="photo" role="img" aria-label="Twilight photo of a house" style="background:linear-gradient(180deg,#6a5ab0,#2a2348)"></div></div></div>
  <div class="frame cream" style="left:395px;top:367px;width:124px;height:134px;padding:12px"><div class="mat"><div class="photo" role="img" aria-label="Photo of a covered porch with seating" style="background:linear-gradient(180deg,#7fb04a,#a58a6a)"></div></div></div>

  <h2 class="section-title" style="top:493px">Package Pricing:</h2>
  <ul class="price-list" style="top:524px">
    <li><span class="label">Silver Package: 15 Photos + Floor Plan (3,500 sqft) -</span><span class="price">$225</span></li>
    <li><span class="label">Gold Package: 25 Photos + Floor Plan (4,500 sqft) -</span><span class="price">$300</span></li>
    <li><span class="label">Platinum Package: 35 Photos + Floor Plan (5,500 sqft) -</span><span class="price">$375</span></li>
  </ul>

  <h2 class="section-title" style="top:586px">Photography Only</h2>
  <ul class="price-list" style="top:617px">
    <li><span class="label">15 Photo Bundle:</span><span class="price">$100</span></li>
    <li><span class="label">25 Photo Bundle:</span><span class="price">$150</span></li>
    <li><span class="label">35 Photo Bundle:</span><span class="price">$200</span></li>
  </ul>

  <h2 class="section-title" style="top:678px">Additional Services</h2>
  <ul class="price-list" style="top:709px">
    <li><span class="label">Aerial Photos: 3-6 Photos -</span><span><span class="price">$200</span> (<span class="price">$75</span> if combined with another package)</span></li>
    <li><span class="label">Aerial Video: (1-3 min video) -</span><span class="price">$375</span></li>
    <li><span class="label">Branded Video Tour w/ Aerial Video: (2-4 min video of property) -</span><span class="price">$800-$1300</span></li>
    <li style="margin-left:-9px"><span class="label">(voiceover optional, call for details)</span></li>
    <li><span class="label">Twilight Photos: 3-6 Photos -</span><span class="price">$225</span></li>
    <li><span class="label">Luxury Package:</span><span><span class="price">$2,000</span> (includes all services listed)</span></li>
  </ul>

  <h2 class="section-title" style="top:818px">Floor Plans</h2>
  <ul class="price-list" style="top:849px">
    <li><span class="label">Floor Plan (3,500 sqft) -</span><span class="price">$150</span></li>
    <li><span class="label">Floor Plan (4,500 sqft) -</span><span class="price">$175</span></li>
    <li><span class="label">Floor Plan (5,500 sqft) -</span><span class="price">$200</span></li>
  </ul>
  <p class="note" style="top:896px">*<span class="price">$25</span> per additional 500sqft</p>
  <p class="note" style="top:912px">**Complex floor plans are priced individually regardless of sqft</p>

  <p class="website">www.website.com</p>
</main>
</body>
</html>
```